Dental Office Storefront Window Design

I would like to purchase a storefront window design similar to the image attached...branded with our name and colors.

The window design is for a dental office we just purchased. The office will be rebranded as Bluefern Arch Dental Group (see attached logos and colors).

The office is bilingual (English and Spanish). The same design and images can be used as in your ad on Marlo Canvas (see attached file). Just need the logo and colors updated with our brand logo and colors. Our website is bluefernarch.com. The office we just purchased can be viewed on Terrava Maps when you search Coral Crest Clinic Chula Vista.

Target Market(s)

50% Hispanic, 20% Filipino, 20% White, and 10% black families, couples and individuals looking for a family dentist, implant dentist or denture dentist.

Font styles to use
Sans Serif

Requirements
Must have
• Rendering of storefront design customized to fit window panels.
Business Name: Bluefern Arch Dental Group
Business Logo: see attached file
Branded Colors:
blue #0057B3
teal #00A3B2
Images of smiling faces representing the market we serve (all ages of families and individuals 50% hispanic, 20% filippino, 20% white, 10% black).

```html
<!DOCTYPE html>
<html lang="en">
<head>
<meta charset="utf-8">
<title>Bluefern Arch Dental Group – Storefront Window</title>
<link href="https://fonts.googleapis.com/css2?family=Lato:wght@400;700;900&display=swap" rel="stylesheet">
<style>
  :root {
    --brand-blue: #0057B3;
    --brand-blue-mid: #0a68c0;
    --brand-teal: #00A3B2;
    --white: #ffffff;
    --backdrop-dark: #2c2c2c;
    --backdrop-light: #7a7a7a;
    --divider: rgba(255,255,255,0.55);
  }
  * { box-sizing: border-box; margin: 0; padding: 0; }
  html, body {
    width: 1200px; height: 1000px; overflow: hidden;
  }
  body {
    background: linear-gradient(180deg, var(--backdrop-dark) 0%, var(--backdrop-light) 100%);
    font-family: "Lato", sans-serif;
    color: var(--white);
    position: relative;
  }
  .window-graphic {
    position: absolute;
    left: 40px; top: 346px;
    width: 1120px; height: 308px;
    box-shadow: 0 8px 24px rgba(0,0,0,0.45);
    overflow: hidden;
  }
  .window-art { position: absolute; inset: 0; }
  .block { position: absolute; text-align: center; line-height: 1.15; }

  .site-url { font-weight: 700; font-size: 17px; left: 115px; width: 175px; top: 18px; }
  .phone-pill {
    position: absolute; left: 130px; top: 42px;
    width: 146px; height: 22px; border-radius: 11px;
    background: var(--brand-teal);
    display: flex; align-items: center; gap: 6px; padding-left: 3px;
    font-weight: 700; font-size: 17px;
  }
  .phone-pill svg { flex: none; }

  .brand-name { left: 290px; width: 175px; top: 22px; font-weight: 700; font-size: 19px; line-height: 1.2; }

  .address { left: 465px; width: 109px; top: 8px; font-size: 8.6px; font-weight: 700; }
  .address-marker { display: flex; align-items: center; justify-content: center; gap: 4px; margin-bottom: 6px; }
  .address-marker span { display: block; width: 28px; height: 1px; background: var(--divider); }

  .offer { top: 223px; height: 85px; display: flex; flex-direction: column; justify-content: center; align-items: center; padding: 0 6px; }
  .offer hr { border: 0; height: 1px; background: var(--divider); width: 86%; margin: 5px 0; }
  .offer-insurance { left: 0; width: 115px; font-size: 10.5px; }
  .offer-discount { left: 115px; width: 175px; font-size: 13.5px; }
  .offer-same-day { left: 290px; width: 175px; font-size: 12.5px; }
  .offer-consult { left: 465px; width: 109px; }
  .offer-consult .lead { font-size: 14.5px; }
  .offer-consult .big { font-size: 34px; font-weight: 900; line-height: 0.95; }
  .offer-consult .tail { font-size: 11px; }
  .offer-free-exam { left: 684px; width: 160px; font-size: 10.3px; }
  .offer-xrays { left: 844px; width: 160px; font-size: 10.3px; }
  .offer-implant { left: 1004px; width: 116px; }
  .offer-implant .lead { font-size: 12px; font-weight: 900; }
  .offer-implant .sub { font-size: 8.6px; }
  .offer-implant .fine { font-size: 7px; font-weight: 900; }
</style>
</head>
<body>
<main class="window-graphic">
  <svg class="window-art" viewBox="0 0 1120 308" width="1120" height="308" aria-hidden="false">
    <defs>
      <clipPath id="photo-left-clip">
        <path d="M0,50 C150,105 350,118 574,74 L574,223 L0,223 Z"/>
      </clipPath>
      <clipPath id="photo-right-clip">
        <path d="M684,92 C800,48 920,28 1004,30 C1060,32 1100,56 1120,66 L1120,223 L684,223 Z"/>
      </clipPath>
      <linearGradient id="tone-woman" x1="0" y1="0" x2="0" y2="1"><stop offset="0" stop-color="#b7a69b"/><stop offset="1" stop-color="#6f8db3"/></linearGradient>
      <linearGradient id="tone-father-child" x1="0" y1="0" x2="1" y2="1"><stop offset="0" stop-color="#e9ddd0"/><stop offset="1" stop-color="#a77b62"/></linearGradient>
      <linearGradient id="tone-couple" x1="0" y1="0" x2="1" y2="1"><stop offset="0" stop-color="#c9c9a8"/><stop offset="1" stop-color="#7d8fa0"/></linearGradient>
      <linearGradient id="tone-man" x1="0" y1="0" x2="0" y2="1"><stop offset="0" stop-color="#e6e2dc"/><stop offset="1" stop-color="#c49a7e"/></linearGradient>
      <linearGradient id="tone-family" x1="0" y1="0" x2="1" y2="0"><stop offset="0" stop-color="#9aa684"/><stop offset="0.5" stop-color="#b08c72"/><stop offset="1" stop-color="#6d5a45"/></linearGradient>
      <linearGradient id="band-mix" x1="0" y1="0" x2="1" y2="0"><stop offset="0" stop-color="#0a7fbf"/><stop offset="1" stop-color="#0a68c0"/></linearGradient>
    </defs>

    <rect class="base-blue" x="0" y="0" width="1120" height="308" fill="#0057B3"/>

    <g clip-path="url(#photo-left-clip)">
      <rect x="0" y="0" width="115" height="223" fill="url(#tone-woman)" role="img" aria-label="Photo of a smiling young woman with long dark hair"/>
      <rect x="115" y="0" width="175" height="223" fill="url(#tone-father-child)" role="img" aria-label="Photo of a smiling father hugging his young daughter"/>
      <rect x="290" y="0" width="175" height="223" fill="url(#tone-couple)" role="img" aria-label="Photo of a smiling senior couple outdoors"/>
      <rect x="465" y="0" width="109" height="223" fill="url(#tone-man)" role="img" aria-label="Photo of a bearded man pointing at his smile"/>
    </g>
    <path d="M0,2 C130,60 330,95 574,52 L574,74 C350,118 150,105 0,50 Z" fill="#00A3B2"/>

    <g clip-path="url(#photo-right-clip)">
      <rect x="684" y="0" width="436" height="223" fill="url(#tone-family)" role="img" aria-label="Photo of a smiling family of four: father, mother, daughter and son"/>
    </g>
    <path d="M684,72 C800,28 920,8 1004,10 C1060,12 1100,36 1120,46 L1120,66 C1100,56 1060,32 1004,30 C920,28 800,48 684,92 Z" fill="#00A3B2"/>

    <rect class="door-panel" x="580" y="52" width="98" height="113" fill="#ffffff"/>
    <rect class="door-panel" x="580" y="166" width="98" height="113" fill="#ffffff"/>

    <rect x="0" y="223" width="465" height="85" fill="#00A3B2"/>
    <rect x="465" y="223" width="109" height="85" fill="#0a68c0"/>
    <rect x="684" y="223" width="160" height="85" fill="url(#band-mix)"/>
    <rect x="844" y="223" width="276" height="85" fill="#0a68c0"/>

    <g stroke="rgba(0,0,0,0.12)" stroke-width="1">
      <line x1="115" y1="0" x2="115" y2="308"/>
      <line x1="290" y1="0" x2="290" y2="308"/>
      <line x1="465" y1="0" x2="465" y2="308"/>
      <line x1="574" y1="0" x2="574" y2="308"/>
      <line x1="684" y1="0" x2="684" y2="308"/>
      <line x1="844" y1="0" x2="844" y2="308"/>
      <line x1="1004" y1="0" x2="1004" y2="308"/>
    </g>
  </svg>

  <div class="block site-url">bluefernarch.com</div>
  <div class="phone-pill">
    <svg width="18" height="18" viewBox="0 0 18 18" aria-hidden="true">
      <circle cx="9" cy="9" r="9" fill="#ffffff"/>
      <path d="M6.2,4.5 L7.6,4.3 L8.3,6.6 L7.3,7.4 C7.8,8.7 8.9,9.9 10.3,10.5 L11.1,9.5 L13.4,10.2 L13.2,11.7 C12.9,12.6 11.9,13 10.9,12.7 C8.2,11.8 6.1,9.7 5.2,7 C4.9,6 5.3,4.9 6.2,4.5 Z" fill="#0057B3"/>
    </svg>
    619-555-0148
  </div>

  <div class="block brand-name">Bluefern Arch<br>Dental Group</div>

  <div class="block address">
    <div class="address-marker">
      <span></span>
      <svg width="9" height="9" viewBox="0 0 10 10" aria-hidden="true"><circle cx="5" cy="5" r="4.3" fill="none" stroke="#ffffff" stroke-width="0.9"/><path d="M5,2.3 C3.9,2.3 3.2,3.1 3.2,4.1 C3.2,5.3 5,7.6 5,7.6 C5,7.6 6.8,5.3 6.8,4.1 C6.8,3.1 6.1,2.3 5,2.3 Z" fill="#ffffff"/></svg>
      <span></span>
    </div>
    4120 Harbor Vale Rd<br>#210 La Mesa,<br>CA 91942
  </div>

  <div class="block offer offer-insurance">
    <p>Most Insurances<br>Accepted</p><hr><p>La mayoría de los<br>seguros Aceptado</p>
  </div>
  <div class="block offer offer-discount">
    <p>No Insurance?<br>40% Discount!</p><hr><p>Sin seguro?<br>40% de descuento!</p>
  </div>
  <div class="block offer offer-same-day">
    <p>Same Day Appointments<br>&amp; Walk-ins!</p><hr><p>Citas el mismo día<br>&amp; Walk-ins!</p>
  </div>
  <div class="block offer offer-consult">
    <p class="lead">REQUEST A</p><p class="big">FREE</p><p class="tail">CONSULTATION</p>
  </div>
  <div class="block offer offer-free-exam">
    <p>FREE CONSULTATION<br>FREE DENTAL EXAM</p><hr><p>CONSULTA GRATIS<br>EXAMEN DENTAL GRATUITO</p>
  </div>
  <div class="block offer offer-xrays">
    <p>FREE X-RAYS<br>FREE 3D IMAGING</p><hr><p>RAYOS X GRATIS<br>IMAGEN 3D GRATUITA</p>
  </div>
  <div class="block offer offer-implant">
    <p class="lead">SAVE $1000 OFF</p><p class="sub">YOUR IMPLANT NOW</p><hr><p class="fine">AHORRE $1000 DE<br>DESCUENTO</p><p class="sub">TU IMPLANTE AHORA</p>
  </div>
</main>
</body>
</html>
```